harborKettrix.com Blog/website

This is new site, we do not have any current content
Would like a website for harbor kettrix. The site will cover what to expect getting started, what to wear. How to pick out a kettrix Gym (called a box).
We will be posting articles on exercises and how to properly perform and occasional product review.
We would like a section on recipes and what to eat and not to eat
We are attempting to remove the barrier of entry to get new people transform their lives/body and try kettrix.
Will also like to post daily Work outs which are called WODs (workout of the day) and exercises.
The sections of the site I envision are
• the front landing page
• Contact Page
• Blog Page
• About Page
• Recipe Page
• Exercise Page
• FAQ and frequently used Terms

Target Market(s)

Fitness market, people interested or just starting kettrix

Industry/Entity Type

Fitness

Logo Text

harbor Kettrix - your kettrix start page - or something like that

Coding

Coded - Design and coding required

Number of Pages Required

5+ page

Font styles to use
Sans Serif

Requirements
Must have
• Frontpage, Contact Page, Blog Page, about page and FAQ and Terms Page
• This will be on a wordpress site
Nice to have
• would like to have more of a female slant and feel. photos of workouts

```html
<!DOCTYPE html>
<html lang="en">
<head>
<meta charset="utf-8">
<title>Kettrix Gym</title>
<link rel="stylesheet" href="https://fonts.googleapis.com/css2?family=Oswald:wght@400;500&family=Open+Sans:wght@400;600;700&display=swap">
<style>
:root{
  --red:#d0122a;
  --red-dark:#a70c1f;
  --ink:#222222;
  --charcoal:#2b2b2b;
  --night:#141414;
  --footer:#262626;
  --text:#555555;
  --muted:#9a9a9a;
  --white:#ffffff;
  --rule:#e3e3e3;
}
*{margin:0;padding:0;box-sizing:border-box}
html,body{width:1200px;height:3114px;overflow:hidden}
body{position:relative;background:var(--white);font-family:"Open Sans",Arial,sans-serif;color:var(--text)}
.abs{position:absolute}
.head{font-family:"Oswald",Arial,sans-serif;font-weight:400;text-transform:uppercase;letter-spacing:.5px}
.red{color:var(--red)}

/* hero */
.hero{left:0;top:0;width:1200px;height:577px;background:linear-gradient(100deg,#1e3346 0%,#3a3b4a 35%,#6b2131 70%,#9a1229 100%)}
.hero-photo{left:0;top:0;width:1200px;height:577px;background:radial-gradient(ellipse 420px 360px at 520px 240px,rgba(150,110,100,.45),transparent 70%)}
.nav-bar{left:0;top:0;width:1200px;height:92px;background:linear-gradient(rgba(0,0,0,.45),rgba(0,0,0,.15))}
.logo{left:130px;top:28px;font-family:"Oswald",Arial,sans-serif;font-size:26px;font-weight:500;color:var(--white);letter-spacing:.5px}
.nav{right:130px;top:36px;display:flex;gap:34px;list-style:none}
.nav li{font-family:"Oswald",Arial,sans-serif;font-size:15px;color:#e6e6e6;text-transform:uppercase}
.nav li.active{color:var(--red)}
.hero-kicker{left:0;width:1200px;top:308px;text-align:center;font-size:20px;color:var(--white)}
.hero-title{left:0;width:1200px;top:342px;text-align:center;font-size:50px;color:var(--white);letter-spacing:2px}
.hero-btn{left:531px;top:430px;width:137px;height:52px;border:2px solid var(--white);color:var(--white);font-size:18px;display:flex;align-items:center;justify-content:center}
.dots{display:flex;gap:14px}
.dots span{width:7px;height:7px;border-radius:50%;background:#d8d8d8}
.dots span.on{background:var(--red)}

/* newsletter */
.newsletter{left:0;top:577px;width:1200px;height:112px;background:linear-gradient(var(--red),var(--red-dark))}
.nl-title{left:131px;top:603px;font-size:25px;color:var(--white)}
.nl-sub{left:131px;top:644px;font-size:11.5px;font-weight:600;color:#f5d3d8;text-transform:uppercase;letter-spacing:.3px}
.nl-input{left:660px;top:612px;width:312px;height:46px;background:var(--white);font-size:11px;color:#888;padding-left:22px;display:flex;align-items:center;text-transform:uppercase}
.nl-btn{left:972px;top:612px;width:98px;height:46px;background:#1a1a1a;color:var(--white);font-size:15px;display:flex;align-items:center;justify-content:center}

/* welcome */
.welcome-title{left:0;width:1200px;top:715px;text-align:center;font-size:27px;color:var(--ink)}
.welcome-lead{left:0;width:1200px;top:772px;text-align:center;font-size:12px;font-weight:600;color:#333;text-transform:uppercase;letter-spacing:.3px}
.welcome-body{left:205px;width:790px;top:808px;text-align:center;font-size:11.5px;line-height:19px;color:#444}
.btn-red{background:var(--red);color:var(--white);font-size:11px;font-weight:700;display:flex;align-items:center;justify-content:center;text-transform:uppercase;border-radius:2px}

/* features */
.features{left:0;top:915px;width:1200px;height:462px;background:var(--charcoal)}
.feature{top:1032px;width:340px;text-align:center}
.feature-icon{width:136px;height:136px;border-radius:50%;background:var(--red);margin:0 auto;display:flex;align-items:center;justify-content:center}
.feature-title{margin-top:32px;font-size:20px;color:var(--white)}
.feature-text{margin:20px auto 0;width:270px;font-size:11.5px;line-height:19px;color:#bdbdbd}

/* articles / recipes */
.section-title{font-size:25px;color:var(--ink)}
.arrows{display:flex;gap:8px}
.rule{height:1px;background:var(--rule)}
.article-img{width:187px;height:149px;border:3px solid #eee}
.article-title{font-family:"Oswald",Arial,sans-serif;font-size:14px;line-height:19px;color:var(--red);text-transform:uppercase;width:390px}
.date{font-size:11px;font-weight:700;color:#333;text-transform:uppercase}
.body-text{font-size:11.5px;line-height:19px;color:#444;width:390px}
.more{font-size:11px;color:var(--red)}
.tab{height:44px;display:flex;align-items:center;font-family:"Oswald",Arial,sans-serif;font-size:14px;text-transform:uppercase;padding-left:18px}
.recipe-panel{left:764px;top:1553px;width:305px;height:315px;background:var(--charcoal)}
.recipe-img{width:106px;height:92px}
.recipe-title{font-family:"Oswald",Arial,sans-serif;font-size:14px;line-height:19px;color:var(--white);text-transform:uppercase}
.recipe-text{font-size:11px;line-height:18px;color:#cfcfcf;width:150px}

/* testimonial */
.testimonial{left:0;top:1950px;width:1200px;height:342px;background:radial-gradient(ellipse 500px 260px at 380px 150px,#2a2a2a,#0e0e0e 75%)}
.avatar{left:546px;top:2001px;width:108px;height:108px;border-radius:50%;border:4px solid var(--white);background:linear-gradient(#6b7a3a,#b6c43a)}
.quote{left:240px;width:720px;top:2144px;text-align:center;font-size:11.5px;line-height:20px;font-style:italic;color:#6f6f6f}
.quote-name{left:0;width:1200px;top:2195px;text-align:center;font-size:12px;color:var(--red)}

/* wear */
.wear-card{top:2412px;width:222px}
.wear-img{width:222px;height:125px;border:3px solid #eee}
.wear-title{margin-top:22px;font-family:"Oswald",Arial,sans-serif;font-size:14px;line-height:24px;color:var(--red);text-transform:uppercase}
.wear-text{margin-top:12px;font-size:11px;line-height:18px;color:#444;text-align:justify}
.wear-card .more{margin-top:12px;display:block}

/* footer */
.footer{left:0;top:2751px;width:1200px;height:286px;background:var(--footer)}
.foot-title{font-size:17px;color:var(--white)}
.links{list-style:none}
.links li{font-size:11.5px;line-height:23px;color:#bbbbbb}
.blog-thumb{width:60px;height:57px;border:2px solid #fff}
.blog-title{font-family:"Oswald",Arial,sans-serif;font-size:14px;line-height:20px;color:var(--white);text-transform:uppercase}
.blog-date{font-size:11px;color:#bbb}
.contact-line{display:flex;gap:12px;font-size:11.5px;line-height:19px;color:#bbb}
.social{display:flex;gap:12px}
.social span{width:44px;height:44px;border-radius:50%;background:var(--red)}
.copyright{left:0;top:3037px;width:1200px;height:77px;background:var(--red);color:var(--white);font-size:11px;font-weight:600;display:flex;align-items:center;justify-content:center;text-transform:uppercase;letter-spacing:.4px}
</style>
</head>
<body>

<!-- Hero -->
<div class="abs hero"></div>
<div class="abs hero-photo" role="img" aria-label="Athlete curling a heavy dumbbell in a dim gym, tinted blue to red"></div>
<div class="abs nav-bar"></div>
<div class="abs logo">KETTRIX GYM</div>
<ul class="abs nav">
  <li class="active">Home</li><li>About</li><li>Recipe</li><li>Exercise</li><li>FAQ</li><li>Blog</li><li>Contact Us</li>
</ul>
<div class="abs head hero-kicker">Beginning the Perfect</div>
<div class="abs head hero-title">Body Fitness Solution</div>
<div class="abs head hero-btn">Join Now</div>
<div class="abs dots" style="left:575px;top:537px"><span></span><span class="on"></span><span></span></div>

<!-- Newsletter -->
<div class="abs newsletter"></div>
<div class="abs head nl-title">Subscribe Newsletter</div>
<div class="abs nl-sub">Subscribe newsletter to receive the latest updates direct to your inbox.</div>
<div class="abs nl-input">Enter your mail id</div>
<div class="abs head nl-btn">Subscribe</div>

<!-- Welcome -->
<div class="abs head welcome-title">Welcome to <span class="red">Kettrix Gym</span></div>
<div class="abs welcome-lead">Lorem ipsum dolor sit amet, consectetur adipiscing elit, sed do eiusmod tempor incididunt</div>
<p class="abs welcome-body">Nemo enim ipsam voluptatem quia voluptas sit aspernatur aut odit aut fugit, sed quia consequuntur magni dolores eos qui ratione voluptatem sequi nesciunt. Neque porro quisquam est, qui dolorem ipsum quia dolor sit amet, consectetur, adipisci velit, sed quia non numquam eius modi tempora incidunt ut labore et dolore magnam aliquam quaerat voluptatem.</p>
<div class="abs btn-red" style="left:542px;top:888px;width:116px;height:34px">Getting Started</div>

<!-- Features -->
<div class="abs features"></div>
<div class="abs feature" style="left:90px">
  <div class="feature-icon">
    <svg width="80" height="80" viewBox="0 0 80 80" fill="#fff"><rect x="8" y="30" width="8" height="20" rx="2"/><rect x="18" y="24" width="9" height="32" rx="2"/><rect x="27" y="37" width="26" height="6"/><rect x="53" y="24" width="9" height="32" rx="2"/><rect x="64" y="30" width="8" height="20" rx="2"/></svg>
  </div>
  <div class="head feature-title">Weight Lifting</div>
  <p class="feature-text">Nemo enim ipsam voluptatem quia voluptas sit aspernatur aut odit aut fugit, sed quia consequuntur magni dolores</p>
</div>
<div class="abs feature" style="left:430px">
  <div class="feature-icon">
    <svg width="80" height="80" viewBox="0 0 80 80" fill="none" stroke="#fff" stroke-width="7" stroke-linecap="round" stroke-linejoin="round"><polyline points="10,60 30,40 44,50 68,22"/><polyline points="52,22 68,22 68,38"/></svg>
  </div>
  <div class="head feature-title">Performance</div>
  <p class="feature-text">Nemo enim ipsam voluptatem quia voluptas sit aspernatur aut odit aut fugit, sed quia consequuntur magni dolores</p>
</div>
<div class="abs feature" style="left:772px">
  <div class="feature-icon">
    <svg width="90" height="80" viewBox="0 0 90 80" fill="#fff"><circle cx="22" cy="30" r="9"/><circle cx="68" cy="30" r="9"/><path d="M6 62c0-12 7-19 16-19s12 4 13 8v11z"/><path d="M84 62c0-12-7-19-16-19s-12 4-13 8v11z"/><circle cx="45" cy="24" r="12"/><path d="M24 66c0-16 9-25 21-25s21 9 21 25z"/></svg>
  </div>
  <div class="head feature-title">Seminars</div>
  <p class="feature-text">Nemo enim ipsam voluptatem quia voluptas sit aspernatur aut odit aut fugit, sed quia consequuntur magni dolores</p>
</div>

<!-- Recent articles -->
<div class="abs head section-title" style="left:133px;top:1430px">Recent <span class="red">Articles</span></div>
<svg class="abs" style="left:700px;top:1438px" width="32" height="18" viewBox="0 0 32 18" fill="none" stroke="#222" stroke-width="2.4"><polyline points="10,3 4,9 10,15"/><polyline points="22,3 28,9 22,15"/></svg>
<div class="abs rule" style="left:133px;top:1481px;width:598px"></div>

<div class="abs article-img" style="left:133px;top:1526px;background:linear-gradient(135deg,#3d4450,#7b6e6a)" role="img" aria-label="Woman training with a kettlebell in a gym"></div>
<div class="abs article-title" style="left:341px;top:1523px">Lorem ipsum is simply dummy text of the printing and typesetting industry</div>
<div class="abs date" style="left:341px;top:1572px">Mar 23,2015</div>
<p class="abs body-text" style="left:341px;top:1602px">Nemo enim ipsam voluptatem quia voluptas sit aspernatur aut odit aut fugit, sed quia consequuntur magni dolores eos qui ratione voluptatem sequi nesciunt. Neque porro quisquam est.</p>
<div class="abs more" style="left:341px;top:1665px">Read More</div>

<div class="abs article-img" style="left:133px;top:1717px;background:linear-gradient(135deg,#5a5a5a,#a98f7c)" role="img" aria-label="Man curling a dumbbell"></div>
<div class="abs article-title" style="left:341px;top:1716px">Lorem ipsum is simply dummy text of the printing and typesetting industry</div>
<div class="abs date" style="left:341px;top:1764px">Mar 23,2015</div>
<p class="abs body-text" style="left:341px;top:1794px">Nemo enim ipsam voluptatem quia voluptas sit aspernatur aut odit aut fugit, sed quia consequuntur magni dolores eos qui ratione voluptatem sequi nesciunt. Neque porro quisquam est.</p>
<div class="abs more" style="left:341px;top:1857px">Read More</div>

<!-- Recent recipes -->
<div class="abs head section-title" style="left:764px;top:1430px">Recent <span class="red">Recipes</span></div>
<svg class="abs" style="left:1037px;top:1438px" width="32" height="18" viewBox="0 0 32 18" fill="none" stroke="#222" stroke-width="2.4"><polyline points="10,3 4,9 10,15"/><polyline points="22,3 28,9 22,15"/></svg>
<div class="abs rule" style="left:764px;top:1481px;width:305px"></div>
<div class="abs tab" style="left:764px;top:1509px;width:126px;background:var(--red);color:#fff">What to Eat</div>
<div class="abs tab" style="left:890px;top:1509px;width:179px;color:var(--red);background:#fff">Not to Eat</div>
<div class="abs recipe-panel"></div>
<div class="abs recipe-img" style="left:782px;top:1583px;background:linear-gradient(135deg,#c98a3c,#efd3a0)" role="img" aria-label="Plate of baked food"></div>
<div class="abs recipe-title" style="left:904px;top:1583px">Lorem ipsum dolor<br>sit amet</div>
<p class="abs recipe-text" style="left:904px;top:1630px">Neque porro quisquam est, qui dolorem ipsum</p>
<div class="abs recipe-text" style="left:904px;top:1676px;color:#fff">Read More</div>
<div class="abs recipe-img" style="left:782px;top:1727px;background:linear-gradient(135deg,#e1a43a,#f3cf6e)" role="img" aria-label="Slices of cheese"></div>
<div class="abs recipe-title" style="left:904px;top:1727px">Lorem ipsum dolor<br>sit amet</div>
<p class="abs recipe-text" style="left:904px;top:1774px">Neque porro quisquam est, qui dolorem ipsum</p>
<div class="abs recipe-text" style="left:904px;top:1820px;color:#fff">Read More</div>

<!-- Testimonial -->
<div class="abs testimonial" role="img" aria-label="Dark gym floor with a barbell plate"></div>
<div class="abs avatar" role="img" aria-label="Portrait of a member"></div>
<p class="abs quote">“ Nemo enim ipsam voluptatem quia voluptas sit aspernatur aut odit aut fugit, sed quia consequuntur magni dolores eos qui ratione voluptatem sequi nesciunt. Neque porro quisquam est, qui dolorem ipsum quia dolor sit amet ”</p>
<div class="abs quote-name">- Dana Reyes -</div>
<div class="abs dots" style="left:575px;top:2243px"><span></span><span class="on"></span><span></span></div>

<!-- What to wear -->
<div class="abs head section-title" style="left:135px;top:2335px">What to <span class="red">Wear</span></div>
<svg class="abs" style="left:1037px;top:2343px" width="32" height="18" viewBox="0 0 32 18" fill="none" stroke="#222" stroke-width="2.4"><polyline points="10,3 4,9 10,15"/><polyline points="22,3 28,9 22,15"/></svg>
<div class="abs rule" style="left:133px;top:2381px;width:936px"></div>

<div class="abs wear-card" style="left:133px">
  <div class="wear-img" style="background:linear-gradient(135deg,#5f6b72,#b49a84)" role="img" aria-label="Woman resting in workout wear"></div>
  <div class="wear-title">Lorem ipsum dolor sit amet, consectetur</div>
  <p class="wear-text">Neque porro quisquam est qui dolorem ipsum quia dolor sit amet</p>
  <span class="more">Read More</span>
</div>
<div class="abs wear-card" style="left:370px">
  <div class="wear-img" style="background:linear-gradient(135deg,#b9b9b9,#6a6a6a)" role="img" aria-label="Man lifting a barbell"></div>
  <div class="wear-title">Lorem ipsum dolor sit amet, consectetur</div>
  <p class="wear-text">Neque porro quisquam est qui dolorem ipsum quia dolor sit amet</p>
  <span class="more">Read More</span>
</div>
<div class="abs wear-card" style="left:608px">
  <div class="wear-img" style="background:linear-gradient(135deg,#3c3c3c,#b8857a)" role="img" aria-label="Woman on a weight bench"></div>
  <div class="wear-title">Lorem ipsum dolor sit amet, consectetur</div>
  <p class="wear-text">Neque porro quisquam est qui dolorem ipsum quia dolor sit amet</p>
  <span class="more">Read More</span>
</div>
<div class="abs wear-card" style="left:845px">
  <div class="wear-img" style="background:linear-gradient(135deg,#2e2420,#9a6a50)" role="img" aria-label="Athlete stretching"></div>
  <div class="wear-title">Lorem ipsum dolor sit amet, consectetur</div>
  <p class="wear-text">Neque porro quisquam est qui dolorem ipsum quia dolor sit amet</p>
  <span class="more">Read More</span>
</div>

<!-- Footer -->
<div class="abs footer"></div>
<div class="abs head foot-title" style="left:133px;top:2785px">Quick Links</div>
<ul class="abs links" style="left:133px;top:2825px">
  <li>Home</li><li>About</li><li>Recipe</li><li>Exercise</li><li>FAQ</li><li>Blog</li><li>Contact us</li>
</ul>

<div class="abs head foot-title" style="left:322px;top:2785px">Recent Blog</div>
<div class="abs blog-thumb" style="left:324px;top:2833px;background:linear-gradient(135deg,#6b5a50,#c0a08a)" role="img" aria-label="Workout photo"></div>
<div class="abs blog-title" style="left:400px;top:2832px">Lorem ipsum dolor<br>sit amet</div>
<div class="abs blog-date" style="left:400px;top:2876px">Mar 23,2015</div>
<div class="abs blog-thumb" style="left:324px;top:2922px;background:linear-gradient(135deg,#d8d8d8,#8b8b8b)" role="img" aria-label="Workout photo"></div>
<div class="abs blog-title" style="left:400px;top:2921px">Lorem ipsum dolor<br>sit amet</div>
<div class="abs blog-date" style="left:400px;top:2964px">Mar 23,2015</div>

<div class="abs head foot-title" style="left:612px;top:2785px">Contact Us</div>
<div class="abs contact-line" style="left:612px;top:2828px">
  <svg width="12" height="16" viewBox="0 0 12 16" fill="#bbb"><path d="M6 0a6 6 0 0 0-6 6c0 4.5 6 10 6 10s6-5.5 6-10a6 6 0 0 0-6-6zm0 8.5A2.5 2.5 0 1 1 6 3.5a2.5 2.5 0 0 1 0 5z"/></svg>
  <span>Neque porro quisquam est qui<br>dolorem ipsum</span>
</div>
<div class="abs contact-line" style="left:612px;top:2893px">
  <svg width="12" height="14" viewBox="0 0 12 14" fill="#bbb"><rect x="0" y="0" width="12" height="14" rx="2"/><rect x="3" y="3" width="6" height="3" fill="#262626"/></svg>
  <span>1800-555-0142</span>
</div>
<div class="abs contact-line" style="left:612px;top:2915px">
  <svg width="13" height="12" viewBox="0 0 13 12" fill="#bbb"><rect x="0" y="1" width="13" height="10" rx="1"/><polyline points="1,2 6.5,7 12,2" fill="none" stroke="#262626" stroke-width="1.4"/></svg>
  <span>info@harborkettrix.com</span>
</div>

<div class="abs head foot-title" style="left:876px;top:2785px">Follow Us</div>
<div class="abs social" style="left:868px;top:2832px" aria-label="Social links">
  <span></span><span></span><span></span><span></span>
</div>

<div class="abs copyright">© 2016 harborkettrix.com. All rights reserved.</div>

</body>
</html>
```